Need a pull up Banner to promote a fiction book

We need a design for a pull up banner (850mm x 2000mm) to promote a fiction book (Novel) with the author.

The book is a mystical/mythical/fantacy novel.

will attache images of the novel and the author

need the source fils in ai format

```html
<!DOCTYPE html>
<html lang="en">
<head>
<meta charset="utf-8">
<title>The Heart in Ruin – Pull-up Banner</title>
<link href="https://fonts.googleapis.com/css2?family=Cinzel:wght@400;500&family=Cardo&family=Marcellus&display=swap" rel="stylesheet">
<style>
  :root {
    --sky-top: #c9ccd1;
    --sky-mid: #e8ebef;
    --sky-cool: #8fa3b8;
    --dusk-warm: #e9b27a;
    --night: #0b0f18;
    --night-blue: #121a2c;
    --title-deep: #0c2966;
    --title-bright: #2f68b8;
    --ink: #111418;
    --gold: #e2a24e;
    --name-light: #f1f2f4;
    --ornament: #1d3a6a;
  }
  * { margin: 0; padding: 0; box-sizing: border-box; }
  html, body { width: 667px; height: 1200px; overflow: hidden; background: #d9d9d9; }

  .banner {
    position: relative;
    width: 667px;
    height: 1200px;
    overflow: hidden;
  }
  .banner__backdrop {
    position: absolute; inset: 0;
    background:
      radial-gradient(ellipse 70% 22% at 20% 62%, rgba(233,178,122,.85), rgba(233,178,122,0) 70%),
      radial-gradient(ellipse 50% 30% at 95% 62%, rgba(120,145,170,.8), rgba(120,145,170,0) 70%),
      linear-gradient(180deg, var(--sky-top) 0%, #d7dbe0 12%, var(--sky-mid) 38%, #dfe2e6 52%, #b9bfc6 64%, #3a4250 74%, var(--night-blue) 80%, var(--night) 100%);
  }

  .title {
    position: absolute; left: 0; right: 0; top: 58px;
    text-align: center;
    font-family: "Cinzel", serif;
    font-weight: 400;
    line-height: .86;
    background: linear-gradient(180deg, var(--title-bright) 0%, var(--title-deep) 55%, #2a5aa6 100%);
    -webkit-background-clip: text; background-clip: text;
    color: transparent;
  }
  .title__line { display: block; }
  .title__line--small { font-size: 74px; margin: 6px 0; }
  .title__line--large { font-size: 138px; }

  .subtitle {
    position: absolute; left: 0; right: 0; top: 440px;
    text-align: center;
    font-family: "Cardo", serif;
    font-size: 44px;
    color: var(--ink);
  }

  .feature-photo {
    position: absolute; left: 160px; top: 520px;
    width: 350px; height: 490px;
    border-radius: 160px 160px 6px 6px;
    background: linear-gradient(180deg, rgba(70,55,50,.55) 0%, rgba(25,25,30,.85) 45%, rgba(60,80,110,.75) 75%, rgba(20,25,40,.6) 100%);
  }

  .byline {
    position: absolute; left: 0; right: 0; top: 1026px;
    text-align: center;
  }
  .byline__lead {
    font-family: "Cardo", serif;
    font-size: 28px;
    color: var(--gold);
  }
  .byline__author {
    margin-top: 4px;
    font-family: "Marcellus", serif;
    font-size: 36px;
    letter-spacing: 1px;
    color: var(--name-light);
  }

  .ornament-band {
    position: absolute; left: 0; right: 0; bottom: 0; height: 90px;
    background: linear-gradient(180deg, rgba(29,58,106,0) 0%, rgba(29,58,106,.55) 60%, rgba(29,58,106,.35) 100%);
  }
</style>
</head>
<body>
  <main class="banner">
    <div class="banner__backdrop" role="img" aria-label="Cloudy dusk sky fading into a dark castle skyline"></div>

    <h1 class="title">
      <span class="title__line title__line--small">THE</span>
      <span class="title__line title__line--large">HEART</span>
      <span class="title__line title__line--small">IN</span>
      <span class="title__line title__line--large">RUIN</span>
    </h1>
    <p class="subtitle">A New Age of Veloran</p>

    <div class="feature-photo" role="img" aria-label="Portrait of the author with the novel shown as a paperback, tablet and phone"></div>

    <div class="byline">
      <p class="byline__lead">A Novel by</p>
      <p class="byline__author">MIRA CASTELL DORAN</p>
    </div>

    <div class="ornament-band" role="img" aria-label="Ornate blue wrought-iron scrollwork along the base"></div>
  </main>
</body>
</html>
```